Please create a custom website design for Cedar Links Institute.

We need a 2 page design.

1. page
Home

Blue Logo
Headline: Home, instructors, Programs, Teaching Video
Club reviews, Event, Member's area, Contact & Location

Please combine 3 coaches golf swing (attached) to one big picture and use other background maybe a golf course or something

3-4 video thumbnails links(Photo attached)
title: About Cedar links,Instrutional video, Club reviews, Event etc.

Welcome to cedar links......
Members Voice

Footline:
Partners Varnholt, Swingpath, QEL rollbox...etc

2. page

Instructors (Photo attached )

Darren Okoye (Blue shirt) Photo + 1 video Thumbnail
Founder/ Director
WLFA Tour Pro/Teaching Pro (A)
ICMRB Lv 3 Certified Instrutor
Trained at Rolf Ebbing School of Golf
Trained at Japan Kawanobeyama Country club
Harbourline Institute of Technology

Tessa Marlow (white shirt) Photo + 1 video Thumbnail
Teaching Director/Head Coach
Teaching Director/Head coach
- Member of European KFLA
Member of Germany KFLA
Member of UK KFLA
ICMRB Lv3 Certified Instructor
Europe Emerging Circuit(1999-02)

Felix Ortan(black shirt) Photo + 1 video Thumbnail

WLFA Teaching Pro (A)
WLFA National Mentor Shield Champion2014
Brookvale Golf College Australia

The logo is attached to this brief.

Preferred colours could be based on Blue
Here is the link to the logo project: http://briefs.pixelvenue.example/task.aspx?id=413577

Target Market(s)

Golfers

Industry/Entity Type

Golf Course

Number of Pages Required

2 page

Font styles to use
Sans Serif

Colors
0555a3
ffffff
ec2027

Requirements
Must have
• The photos provided
• Blue based Webpage
Nice to have
• Other golf photos
• a little touch of red color

```html
<!DOCTYPE html>
<html lang="en">
<head>
<meta charset="utf-8">
<title>Cedar Links Institute</title>
<link href="https://fonts.googleapis.com/css2?family=Mulish:wght@400;600&family=Open+Sans:wght@400&display=swap" rel="stylesheet">
<style>
:root{
  --navy-deep:#021a52;
  --navy:#0a2d78;
  --nav-top:#2064c8;
  --nav-bottom:#0b3f9c;
  --red:#c8161d;
  --red-title:#d0141b;
  --ink:#333;
  --body:#555;
  --line:#dcdcdc;
  --white:#fff;
  --foot:#f3f3f3;
}
*{margin:0;padding:0;box-sizing:border-box}
html,body{width:1065px;height:1200px;overflow:hidden;background:var(--white)}
body{position:relative;font-family:'Mulish',sans-serif;color:var(--ink)}
.header-band{position:absolute;left:0;top:0;width:1065px;height:290px;
  background:radial-gradient(ellipse 420px 200px at 230px 60px,#0f4bb0 0%,rgba(15,75,176,0) 100%),linear-gradient(180deg,var(--navy) 0%,var(--navy-deep) 100%)}
.brand{position:absolute;left:114px;top:38px;display:flex;align-items:center;gap:8px;color:var(--white)}
.brand-mark{width:48px;height:48px;border:3px solid var(--white);border-radius:50%}
.brand-name{font-weight:600;font-size:33px;line-height:1;letter-spacing:-0.5px}
.brand-sub{font-size:11.5px;letter-spacing:10px;margin-top:1px;padding-left:23px}
.social-top{position:absolute;left:868px;top:79px;display:flex;gap:6px}
.social-top span{width:21px;height:21px;border-radius:2px;background:#3b6fb6}
.social-top span:first-child{background:#c4302b}
.main-nav{position:absolute;left:104px;top:112px;width:849px;height:48px;display:flex;
  background:linear-gradient(180deg,var(--nav-top),var(--nav-bottom));border-radius:3px 3px 0 0}
.main-nav a{color:var(--white);text-decoration:none;font-size:16px;display:flex;align-items:center;justify-content:center;white-space:nowrap;
  border-right:1px solid rgba(0,20,80,.55);box-shadow:1px 0 0 rgba(255,255,255,.12)}
.main-nav a:last-child{border:none;box-shadow:none}
.hero{position:absolute;left:104px;top:160px;width:849px;height:381px;border-radius:0 0 6px 6px;overflow:hidden;
  background:linear-gradient(100deg,#a99a62 0%,#6f7a3e 30%,#9b8a6a 55%,#3c3a3a 80%,#5a5448 100%)}
.hero-caption{position:absolute;left:44px;top:138px;width:327px;height:140px;background:rgba(205,20,27,.88);color:var(--white);padding:19px 0 0 27px}
.hero-caption .kicker{font-size:21px;line-height:1.2}
.hero-caption h1{font-weight:400;font-size:27px;line-height:1.3}
.hero-caption p{font-family:'Open Sans',sans-serif;font-size:10.5px;line-height:18px;margin-top:5px}
.slider-dots{position:absolute;left:397px;top:357px;display:flex;gap:3px}
.slider-dots span{width:12px;height:12px;border-radius:50%;background:var(--white)}
.welcome{position:absolute;left:107px;top:583px;width:500px}
.welcome h2{font-weight:400;font-size:24.5px;color:#3a3a3a;margin-bottom:12px;white-space:nowrap}
.welcome p{font-family:'Open Sans',sans-serif;font-size:10.6px;line-height:16.5px;color:var(--body);margin-bottom:8px;padding-left:3px}
.btn-join{display:inline-block;margin:6px 0 0 2px;width:110px;height:32px;line-height:32px;text-align:center;font-size:12px;color:var(--white);
  background:linear-gradient(180deg,#1552b4,#08347f);border-radius:3px;letter-spacing:-.2px}
.video-frame{position:absolute;left:658px;top:581px;width:291px;height:183px;background:var(--white);border:1px solid var(--line);padding:3px;box-shadow:0 1px 3px rgba(0,0,0,.12)}
.video-thumb{position:relative;width:100%;height:100%;background:linear-gradient(180deg,#9fb6c6 0%,#8da27a 40%,#79a83e 100%)}
.video-thumb svg{position:absolute;left:122px;top:68px}
.divider{position:absolute;left:102px;top:799px;width:854px;height:1px;background:var(--line)}
.features{position:absolute;left:104px;top:838px;display:flex;gap:7px}
.feature-card{width:206px;height:216px;border:1px solid var(--line);border-radius:2px;background:linear-gradient(180deg,#fff 70%,#f1f1f1);box-shadow:0 3px 4px -2px rgba(0,0,0,.12)}
.feature-photo{height:128px}
.feature-card h3{font-weight:400;font-size:19.5px;color:var(--red-title);margin:13px 0 4px 18px;white-space:nowrap}
.feature-card p{font-family:'Open Sans',sans-serif;font-size:9.5px;line-height:16.5px;color:#666;margin-left:19px}
.site-footer{position:absolute;left:0;top:1097px;width:1065px;height:103px;border-top:1px solid var(--line);background:linear-gradient(180deg,#fff,var(--foot))}
.footer-nav{position:absolute;left:116px;top:28px;font-size:12.5px;color:#555}
.footer-nav span{margin:0 5px;color:#777}
.copyright{position:absolute;left:116px;top:53px;font-size:11.5px;color:#666}
.social-foot{position:absolute;left:859px;top:30px;display:flex;gap:8px}
.social-foot span{width:20px;height:20px;border-radius:2px;background:#3b5a9a}
.social-foot span:nth-child(2){background:#40b6e6}
.social-foot span:nth-child(3){background:#1f6fae}
</style>
</head>
<body>
<div class="header-band"></div>
<div class="brand">
  <div class="brand-mark"></div>
  <div><div class="brand-name">Cedar Links</div><div class="brand-sub">INSTITUTE</div></div>
</div>
<div class="social-top" aria-label="Social links"><span></span><span></span><span></span></div>
<nav class="main-nav">
  <a style="width:95px">Home</a>
  <a style="width:105px">About Us</a>
  <a style="width:138px">Golf Coaching</a>
  <a style="width:126px">News &amp; Blog</a>
  <a style="width:167px">Upcoming Classes</a>
  <a style="width:90px">Join Us</a>
  <a style="width:128px">Contact Us</a>
</nav>
<section class="hero" role="img" aria-label="Photo of a golf coach guiding a student's swing on a sunny course">
  <div class="hero-caption">
    <div class="kicker">Lorem ipsum dolor sit</div>
    <h1>Golf Training Academy</h1>
    <p>Curabitur iaculis tempus eros Curabitur vel mi sit amet<br>magna malesuada ultrices Ut nisi erat</p>
  </div>
  <div class="slider-dots"><span></span><span></span><span></span><span></span></div>
</section>
<section class="welcome">
  <h2>Welcome to Cedar Links Institute Mainpage</h2>
  <p>Mauris vel lacus vitae felis vestibulum volutpat Etiam est nunc venenatis in tristique eu imperdiet ac<br>nisl Cum sociis natoque penatibus et magnis dis parturient montes nascetur ridiculus mus In iaculis<br>facilisis massa Etiam eu urna Sed porta Suspendisse quam leo molestie sed</p>
  <p>Luctus quis feugiat in pede Fusce tellus Sed metus augue convallis et vehicula ut pulvinar eu ante<br>Integer orci tellus tristique vitae consequat nec porta vel lectus Nulla sit amet diam</p>
  <a class="btn-join">JOIN US NOW</a>
</section>
<div class="video-frame">
  <div class="video-thumb" role="img" aria-label="Video still of three golfers shaking hands on a green with mountains behind">
    <svg width="40" height="40" viewBox="0 0 40 40"><circle cx="20" cy="20" r="20" fill="#000"/><path d="M16 12 L28 20 L16 28 Z" fill="#fff"/></svg>
  </div>
</div>
<div class="divider"></div>
<section class="features">
  <article class="feature-card">
    <div class="feature-photo" role="img" aria-label="Photo of a golfer putting on a green" style="background:linear-gradient(180deg,#b9cbd6 0%,#8fa466 45%,#97a25a 100%)"></div>
    <h3>Golf Coaching</h3><p>Lorem ipsum dolor sit amet consect-<br>etuer adipis cing elit Nam ut</p>
  </article>
  <article class="feature-card">
    <div class="feature-photo" role="img" aria-label="Photo of an instructor helping a woman with her golf swing" style="background:linear-gradient(180deg,#a9c2cc 0%,#5d8f2c 45%,#6fae2c 100%)"></div>
    <h3>Why Our Academy</h3><p>Lorem ipsum dolor sit amet consect-<br>etuer adipis cing elit Nam ut</p>
  </article>
  <article class="feature-card">
    <div class="feature-photo" role="img" aria-label="Photo of two golfers shaking hands by the flag" style="background:linear-gradient(180deg,#c4d2dc 0%,#7d9fb5 40%,#88ae4a 100%)"></div>
    <h3>Join Us Now</h3><p>Lorem ipsum dolor sit amet consect-<br>etuer adipis cing elit Nam ut</p>
  </article>
  <article class="feature-card">
    <div class="feature-photo" role="img" aria-label="Photo of two golfers holding a trophy on the course" style="background:linear-gradient(180deg,#9fbbc4 0%,#4f7a3a 40%,#b08f86 100%)"></div>
    <h3>News &amp; Media</h3><p>Lorem ipsum dolor sit amet consect-<br>etuer adipis cing elit Nam ut</p>
  </article>
</section>
<footer class="site-footer">
  <div class="footer-nav">Home<span>|</span>About Us<span>|</span>Golf Coaching<span>|</span>News &amp; Blog<span>|</span>Upcoming Classes<span>|</span>Join Us<span>|</span>Contact Us</div>
  <div class="copyright">© 2014 Company Name&nbsp; All right reserved&nbsp; Term of Use</div>
  <div class="social-foot" aria-label="Social links"><span></span><span></span><span></span></div>
</footer>
</body>
</html>
```